Business Card/Design Project for Personal Injury Lawyer

Personal Injury Attorney. I represent people who have been injured in accidents and are making money damage claims against the negligent party. As a personal injury attorney, I am a counselor, advisor, and legal representative to my clients. Clients want someone who is aggresssive yet professional.

More information about what I do an be found at www.vorlandlaw.example

Target Market(s)

General public.

Industry/Entity Type

Legal

Contact Information for Business Card

Need a new logo/brand image for b-cards, website, and letterhead/envelops. Looking for something original (no scales of justice or courthouse columns), yet classy and professional.

Here's what I'm thinking (but I'm always open to other ideas):

On the front, I would like my name (Colton R. Vorland), and underneath the words "Personal Injury Attorney." The background could be black, for example, and the lettering could be white or foil. I'm open to differnt colors, or even two colors. My name on the front side should pop.

And then on the back would be all my contact info, and maybe a logo or a slogan.

Here are two slogans I've come up with so far: 1. Settle for More. 2. Serious Results for the Seriously Injured.

Requirements
Must have
• Something that identifys me as a personal injury attorney, such as the words Personal Injury Attorney (or Lawyer, or Law Firm, etc.).
Nice to have
• A style/image that can be used nicely on my website and on letterhead.
Should not have
• Tired, commonly used logos or symbols, such a scales of justice or courthouse columns.

```html
<!DOCTYPE html>
<html lang="en">
<head>
<meta charset="utf-8">
<title>Vorland Law – Business Cards</title>
<link rel="stylesheet" href="https://fonts.googleapis.com/css2?family=Quicksand:wght@300;400;600&family=Josefin+Sans:wght@300&family=Source+Sans+3:wght@400&display=swap">
<style>
  :root {
    --navy: #1d3a6b;
    --white: #ffffff;
    --firm-blue: #3b9ac4;
    --page: #ffffff;
    --shadow: rgba(0, 0, 0, 0.45);
  }
  html, body {
    margin: 0;
    padding: 0;
    width: 1200px;
    height: 1200px;
    overflow: hidden;
    background: var(--page);
  }
  .sheet {
    position: relative;
    width: 1200px;
    height: 1200px;
  }
  .card {
    position: absolute;
    border-radius: 9px;
    overflow: hidden;
    box-shadow: 5px 6px 7px var(--shadow);
  }
  .card--navy { background: var(--navy); }
  .card--split { background: var(--white); }

  .card-front-h { left: 67px; top: 173px; width: 490px; height: 299px; }
  .card-back-h  { left: 625px; top: 173px; width: 491px; height: 293px; }
  .card-front-v { left: 232px; top: 610px; width: 268px; height: 449px; }
  .card-back-v  { left: 592px; top: 610px; width: 268px; height: 446px; }

  .attorney {
    position: absolute;
    color: var(--white);
    font-family: "Quicksand", sans-serif;
    text-align: right;
  }
  .attorney__name {
    display: block;
    font-weight: 600;
    letter-spacing: 0.02em;
    border-bottom: 2px solid var(--white);
    line-height: 1.05;
    padding-bottom: 2px;
  }
  .attorney__title {
    display: block;
    font-weight: 300;
    letter-spacing: -0.01em;
  }
  .card-front-h .attorney { left: 58px; top: 114px; width: 384px; }
  .card-front-h .attorney__name { font-size: 37px; }
  .card-front-h .attorney__title { font-size: 18px; margin-top: 2px; }
  .card-front-v .attorney { left: 32px; top: 380px; width: 210px; }
  .card-front-v .attorney__name { font-size: 20px; border-bottom-width: 1.5px; }
  .card-front-v .attorney__title { font-size: 10px; margin-top: 1px; }

  .firm {
    position: absolute;
    color: var(--firm-blue);
    text-align: center;
  }
  .firm__name {
    display: block;
    font-family: "Josefin Sans", sans-serif;
    font-weight: 300;
    letter-spacing: 0.02em;
    line-height: 1;
  }
  .firm__tagline {
    display: block;
    font-family: "Quicksand", sans-serif;
    font-weight: 400;
    letter-spacing: 0.14em;
    text-transform: uppercase;
  }
  .card-back-h .firm { left: 97px; top: 52px; width: 330px; }
  .card-back-h .firm__name { font-size: 44px; }
  .card-back-h .firm__tagline { font-size: 13.5px; margin-top: 12px; }
  .card-back-v .firm { left: 34px; top: 246px; width: 200px; }
  .card-back-v .firm__name { font-size: 25px; }
  .card-back-v .firm__tagline { font-size: 7.8px; margin-top: 6px; }

  .contact-band {
    position: absolute;
    left: 0;
    right: 0;
    bottom: 0;
    background: var(--navy);
  }
  .card-back-h .contact-band { top: 151px; }
  .card-back-v .contact-band { top: 316px; }

  .contact {
    position: absolute;
    color: var(--white);
    font-family: "Source Sans 3", sans-serif;
    margin: 0;
    padding: 0;
    list-style: none;
  }
  .contact__row {
    display: flex;
    align-items: center;
    white-space: nowrap;
  }
  .contact__item { display: inline-flex; align-items: center; }
  .contact__sep { margin: 0 7px; }
  .icon { fill: var(--white); flex: none; }

  .card-back-h .contact { left: 44px; top: 70px; font-size: 12px; }
  .card-back-h .contact__row + .contact__row { margin-top: 11px; }
  .card-back-h .icon { width: 11px; height: 11px; margin-right: 8px; }

  .card-back-v .contact { left: 30px; top: 26px; font-size: 10.5px; line-height: 1.3; }
  .card-back-v .contact__row { align-items: flex-start; }
  .card-back-v .contact__row + .contact__row { margin-top: 7px; }
  .card-back-v .icon { width: 10px; height: 10px; margin-right: 9px; margin-top: 2px; }
</style>
</head>
<body>
<main class="sheet">

  <section class="card card--navy card-front-h" aria-label="Card front, landscape">
    <div class="attorney">
      <span class="attorney__name">Colton R. Vorland</span>
      <span class="attorney__title">Personal Injury Attorney</span>
    </div>
  </section>

  <section class="card card--split card-back-h" aria-label="Card back, landscape">
    <div class="firm">
      <span class="firm__name">VORLAND LAW</span>
      <span class="firm__tagline">Personal Injury &amp; Product Liability</span>
    </div>
    <div class="contact-band">
      <ul class="contact">
        <li class="contact__row">
          <svg class="icon" viewBox="0 0 12 12"><path d="M6 0a4 4 0 0 0-4 4c0 3 4 8 4 8s4-5 4-8a4 4 0 0 0-4-4zm0 5.6A1.6 1.6 0 1 1 6 2.4a1.6 1.6 0 0 1 0 3.2z"/></svg>
          420 Harbor Line Ave Suite 300&nbsp; Bayview, Florida 30000
        </li>
        <li class="contact__row">
          <span class="contact__item">
            <svg class="icon" viewBox="0 0 12 12"><path d="M2.5 0.5l2 2.5-1.2 1.3c.7 1.6 2 2.9 3.6 3.6L8.2 6.7l2.5 2-1.2 2.6C5 11 1 7 .7 2.5z"/></svg>
            555.014.2290
          </span>
          <span class="contact__sep">|</span>
          <span class="contact__item">
            <svg class="icon" viewBox="0 0 12 12"><path d="M0 2h12v8H0zm1 1v.4l5 3.3 5-3.3V3zm0 1.6V9h10V4.6L6 8z"/></svg>
            info@vorlandlaw.example
          </span>
          <span class="contact__sep">|</span>
          <span class="contact__item">
            <svg class="icon" viewBox="0 0 12 12"><path d="M6 0a6 6 0 1 0 0 12A6 6 0 0 0 6 0zM1.2 5.4h2.4c.1-1.6.5-3 1.2-4A4.8 4.8 0 0 0 1.2 5.4zm0 1.2a4.8 4.8 0 0 0 3.6 4c-.7-1-1.1-2.4-1.2-4zm3.6 0c.1 1.7.6 3.1 1.2 3.9.6-.8 1.1-2.2 1.2-3.9zm0-1.2h2.4C7.1 3.7 6.6 2.3 6 1.5c-.6.8-1.1 2.2-1.2 3.9zm3.6 0h2.4a4.8 4.8 0 0 0-3.6-4c.7 1 1.1 2.4 1.2 4zm0 1.2c-.1 1.6-.5 3-1.2 4a4.8 4.8 0 0 0 3.6-4z"/></svg>
            www.vorlandlaw.example
          </span>
        </li>
      </ul>
    </div>
  </section>

  <section class="card card--navy card-front-v" aria-label="Card front, portrait">
    <div class="attorney">
      <span class="attorney__name">Colton R. Vorland</span>
      <span class="attorney__title">Personal Injury Attorney</span>
    </div>
  </section>

  <section class="card card--split card-back-v" aria-label="Card back, portrait">
    <div class="firm">
      <span class="firm__name">VORLAND LAW</span>
      <span class="firm__tagline">Personal Injury &amp; Product Liability</span>
    </div>
    <div class="contact-band">
      <ul class="contact">
        <li class="contact__row">
          <svg class="icon" viewBox="0 0 12 12"><path d="M6 0a4 4 0 0 0-4 4c0 3 4 8 4 8s4-5 4-8a4 4 0 0 0-4-4zm0 5.6A1.6 1.6 0 1 1 6 2.4a1.6 1.6 0 0 1 0 3.2z"/></svg>
          <span>420 Harbor Line Ave Suite 300<br>Bayview, Florida 30000.</span>
        </li>
        <li class="contact__row">
          <svg class="icon" viewBox="0 0 12 12"><path d="M2.5 0.5l2 2.5-1.2 1.3c.7 1.6 2 2.9 3.6 3.6L8.2 6.7l2.5 2-1.2 2.6C5 11 1 7 .7 2.5z"/></svg>
          555.014.2290
        </li>
        <li class="contact__row">
          <svg class="icon" viewBox="0 0 12 12"><path d="M6 0a6 6 0 1 0 0 12A6 6 0 0 0 6 0zM1.2 5.4h2.4c.1-1.6.5-3 1.2-4A4.8 4.8 0 0 0 1.2 5.4zm0 1.2a4.8 4.8 0 0 0 3.6 4c-.7-1-1.1-2.4-1.2-4zm3.6 0c.1 1.7.6 3.1 1.2 3.9.6-.8 1.1-2.2 1.2-3.9zm0-1.2h2.4C7.1 3.7 6.6 2.3 6 1.5c-.6.8-1.1 2.2-1.2 3.9zm3.6 0h2.4a4.8 4.8 0 0 0-3.6-4c.7 1 1.1 2.4 1.2 4zm0 1.2c-.1 1.6-.5 3-1.2 4a4.8 4.8 0 0 0 3.6-4z"/></svg>
          www.vorlandlaw.example
        </li>
        <li class="contact__row">
          <svg class="icon" viewBox="0 0 12 12"><path d="M0 2h12v8H0zm1 1v.4l5 3.3 5-3.3V3zm0 1.6V9h10V4.6L6 8z"/></svg>
          info@vorlandlaw.example
        </li>
      </ul>
    </div>
  </section>

</main>
</body>
</html>
```